Poster for the 'LFA Monthly Draw'

We are a parents association for a senior school and have a number of money raising activities.

We require a poster a lucky draw where parents who subscribe £20 for the school year are entered into a monthly cash prize draw.

Draws are performed monthly. Some detail about it is available here

http://www.larchfield.example-school.uk/lfa/what-is-350-circle

We are changing the name from 'The 350 circle' to 'LFA Monthly draw', although we don't need the name change highlighted or noted on the poster

A logo is available on the word document application at the above link. Not sure of the quality. I can look to obtain a better resolution, but no promises.

A brief overview of the LFA can be read here for any thoughts / inspiration.

We don't want any reference to specific items purchased, unless we can easily update this on the poster ourselves.

http://www.larchfield.example-school.uk/lfa

Target Market(s)

Parents of school kids aged 13 to 17 from whom we are trying to raise contributions to so as to provide funding to school departments who have need to additional items that are not available via the school budget.

Industry/Entity Type

School

Requirements
Must have
• LFA Parents association logo, as in the current 350 circle application, should appear.
• Reference to the amount to be contributed of £20 for the year.
• Reference to the monthly prize draw amounts of
• 1st prize - £30
• 2nd prize - £20
• 3rd Prize £10
• Please note all spellings are to be UK english, not American english.
• Payment methods should be highlighted being
• - Trenvolo- via the school website
• - Cash
• - Cheque - Payable to Larchfield’s Parents’ Association 350 Circle
• No specific colour scheme, although you will see from the school website what the colours are and this should have some representation, but not overbearing.
• The following text is to appear
• The LFA Monthly Draw is a fundraiser for the Larchfield Parent Association. We raise funds to provide the best possible resources and facilities, for your children, to enhance their learning.
• Thank you for your support of the LFA
Nice to have
• The font type is not to critical, however, it should be easy to read in a short space of time as people are walking past, so not excessive amounts of text detail and not to small a font.

```html
<!DOCTYPE html>
<html lang="en-GB">
<head>
<meta charset="utf-8">
<title>LFA Monthly Draw</title>
<link href="https://fonts.googleapis.com/css2?family=Bree+Serif&display=swap" rel="stylesheet">
<style>
  :root {
    --maroon: #7a0b2e;
    --maroon-deep: #5a0620;
    --maroon-bright: #a01540;
    --sky: #d3e4f5;
    --sky-light: #eef5fc;
    --ink: #111111;
    --white: #ffffff;
  }
  * { margin: 0; padding: 0; box-sizing: border-box; }
  html, body { width: 848px; height: 1200px; overflow: hidden; }
  body {
    font-family: "Bree Serif", Georgia, serif;
    background: linear-gradient(160deg, var(--sky) 0%, var(--sky-light) 60%, var(--sky) 100%);
    position: relative;
  }
  .poster { position: relative; width: 848px; height: 1200px; }

  .school-mark {
    position: absolute; left: 52px; top: 62px;
    display: flex; flex-direction: column; align-items: center; gap: 14px;
    width: 190px;
  }
  .school-mark__dot {
    width: 120px; height: 120px; border-radius: 50%;
    background: var(--maroon);
  }
  .school-mark__name {
    color: var(--maroon); font-size: 24px; text-align: center; line-height: 1.1;
  }

  .draw-title {
    position: absolute; left: 276px; top: 62px;
    color: var(--maroon); font-size: 55px; line-height: 59px; font-weight: 400;
  }

  .badge {
    position: absolute; border-radius: 50%;
    background: radial-gradient(circle at 40% 35%, var(--maroon-bright) 0%, var(--maroon) 55%, var(--maroon-deep) 100%);
    color: var(--white); display: flex; flex-direction: column;
    align-items: center; justify-content: center; text-align: center;
    box-shadow: 0 0 0 6px var(--white);
  }
  .badge::after {
    content: ""; position: absolute; inset: 9px; border-radius: 50%;
    border: 3px dotted var(--white);
  }
  .badge--headline { left: 543px; top: 15px; width: 280px; height: 280px; font-size: 100px; }
  .badge--prize { width: 212px; height: 212px; top: 945px; }
  .badge--first { left: 57px; }
  .badge--second { left: 318px; }
  .badge--third { left: 578px; }
  .badge__rank { font-size: 36px; line-height: 1; }
  .badge__amount { font-size: 74px; line-height: 1; }

  .band { position: absolute; left: 0; top: 0; width: 848px; height: 1200px; }

  .band-copy {
    position: absolute; left: 40px; top: 448px; width: 820px;
    transform: rotate(-8.7deg); transform-origin: left top;
    color: var(--white);
  }
  .band-copy__headline { font-size: 45px; line-height: 50px; margin-bottom: 26px; }
  .band-copy__body { font-size: 19px; line-height: 25px; margin-left: 18px; }
  .band-copy__thanks { font-size: 19px; margin-left: 38px; margin-top: 30px; }

  .payment {
    position: absolute; right: 38px; top: 716px; text-align: right;
    color: var(--ink); font-size: 18px; line-height: 24px;
  }
  .payment__heading { font-size: 22px; margin-bottom: 4px; }
  .payment__method { color: var(--maroon); font-size: 22px; line-height: 30px; }
  .payment__note { margin-bottom: 6px; }

  .hands-artwork {
    position: absolute; left: 0; top: 880px; width: 848px; height: 320px;
    background: linear-gradient(180deg, rgba(238,245,252,0) 0%, rgba(240,200,170,.55) 40%, rgba(230,120,90,.5) 70%, rgba(250,235,220,.9) 100%);
  }
</style>
</head>
<body>
<main class="poster">
  <div class="hands-artwork" role="img" aria-label="Colourful painted children's hands raised upwards"></div>

  <svg class="band" viewBox="0 0 848 1200" aria-hidden="true">
    <defs>
      <radialGradient id="bandFill" cx="0.45" cy="0.5" r="0.7">
        <stop offset="0" stop-color="#9a1340"/>
        <stop offset="1" stop-color="#5e0722"/>
      </radialGradient>
    </defs>
    <polygon points="0,358 848,228 848,640 0,776" fill="url(#bandFill)"/>
    <line x1="0" y1="348" x2="848" y2="218" stroke="#222" stroke-width="4" stroke-dasharray="3 3"/>
    <line x1="0" y1="786" x2="848" y2="650" stroke="#222" stroke-width="4" stroke-dasharray="3 3"/>
  </svg>

  <div class="school-mark">
    <div class="school-mark__dot"></div>
    <div class="school-mark__name">Larchfield School</div>
  </div>

  <h1 class="draw-title">LFA<br>Monthly<br>Draw</h1>

  <div class="badge badge--headline">£20</div>

  <section class="band-copy">
    <h2 class="band-copy__headline">Contribute £20 for the year<br>to win monthly cash prizes.</h2>
    <p class="band-copy__body">The LFA Monthly Draw is a fundraiser for the Larchfield Parent Association.<br>We raise funds to provide the best possible resources and facilities,<br>for your children, to enhance their learning.</p>
    <p class="band-copy__thanks">Thank you for your support of the LFA</p>
  </section>

  <section class="payment">
    <h3 class="payment__heading">Payment methods</h3>
    <p class="payment__method">Trenvolo</p>
    <p class="payment__note">(via the school website)</p>
    <p class="payment__method">Cash</p>
    <p class="payment__method">Cheque</p>
    <p>(Payable to Larchfield’s Parents’ Association 350 Circle)</p>
  </section>

  <div class="badge badge--prize badge--first"><span class="badge__rank">1st</span><span class="badge__amount">£30</span></div>
  <div class="badge badge--prize badge--second"><span class="badge__rank">2nd</span><span class="badge__amount">£20</span></div>
  <div class="badge badge--prize badge--third"><span class="badge__rank">3rd</span><span class="badge__amount">£10</span></div>
</main>
</body>
</html>
```